Shopping center investment profile

We need to design a two-page 8.5" x 11" brochure that can be used as a template for profiling our shopping centers and demonstrating our track record to investors.

Our company (Pelvoran Real Estate Investments) owns retail shopping centers in the southwestern United States. Our website is www.kelvistrand.example, but we will be redesigning and modernizing the website and logo in the near future, so please do not use the color schemes or framework of the website for the brochure.

Our investors are institutional and high net worth investors who typically have an existing relationship with our company. They are determining whether to invest multi-millions of dollars in a shopping center opportunity, so the brochure needs to be professional, very high quality and provide key information about the specific property.
Updates

Additional guidance on color scheme:

We would like to see a Blue (something like Hex #5A61BC) and Gold (Hex #EDB215) or (Hex #DDA24B) color scheme with some Black accents 

Thank you!

Target Market(s)

Our target audiences are institutional investors, high net-worth individuals, financial firms and medium to large commercial real estate companies.

Industry/Entity Type

Investment

Requirements
Must have
• Clean and modern look with corresponding fonts and colors.
• Incorporates the information found in the attached "Morrowick Commons profile" Pages or PDF file.
• Final file design files that can be modified easily
Nice to have
• Two examples of industry brochures are attached. These are examples of the professional quality that we are looking for, not necessarily the design or format.

```html
<!DOCTYPE html>
<html lang="en">
<head>
<meta charset="utf-8">
<title>Morrowick Commons – Property Profile</title>
<link href="https://fonts.googleapis.com/css2?family=Roboto+Condensed:wght@700&family=Roboto:wght@400&display=swap" rel="stylesheet">
<style>
  :root{
    --blue:#5a61bc;
    --gold:#edb215;
    --black:#1b1b1b;
    --lavender:#dcdcf2;
    --map-grey:#8c8c8f;
    --rule:#c8c8dc;
    --text:#222;
    --white:#fff;
  }
  html,body{margin:0;padding:0;overflow:hidden;background:var(--white);}
  .page{position:relative;width:927px;height:1200px;overflow:hidden;background:var(--white);font-family:"Roboto",Arial,sans-serif;color:var(--text);}
  .abs{position:absolute;}
  .side-band{left:0;top:0;width:204px;height:1200px;}
  .brand-box{left:46px;top:0;width:158px;height:160px;background:var(--gold);}
  .brand-name{left:60px;top:38px;width:140px;font-family:"Roboto",Arial,sans-serif;font-weight:400;color:var(--black);font-size:19px;line-height:21px;}
  .header-band{left:211px;top:0;width:716px;height:160px;background:var(--blue);}
  .title{left:252px;top:36px;margin:0;font-family:"Roboto Condensed",Arial,sans-serif;font-weight:700;font-size:54px;line-height:60px;color:var(--white);letter-spacing:-0.5px;}
  .subtitle{left:252px;top:93px;margin:0;font-family:"Roboto Condensed",Arial,sans-serif;font-weight:700;font-size:26px;color:var(--white);}
  .corner{right:0;top:0;width:210px;height:165px;}
  .profile-tag{right:31px;top:32px;text-align:right;font-family:"Roboto Condensed",Arial,sans-serif;font-weight:700;font-size:21px;line-height:25px;color:var(--black);}
  .photo-frame{left:40px;top:160px;width:887px;height:204px;background:var(--white);}
  .photo{top:167px;height:190px;}
  .photo.before{left:46px;width:431px;background:linear-gradient(180deg,#d7dfea 0%,#c8c1ae 55%,#7f7a72 100%);}
  .photo.after{left:483px;width:444px;background:linear-gradient(180deg,#4f6f9c 0%,#9aaecb 45%,#a7613e 70%,#5b5b60 100%);}
  .caption-band{left:211px;top:363px;width:716px;height:34px;}
  .caption{top:364px;font-family:"Roboto Condensed",Arial,sans-serif;font-weight:700;font-size:21px;color:var(--white);}
  .body-panel{left:211px;top:397px;width:716px;height:409px;background:var(--lavender);}
  .section-title{margin:0;font-family:"Roboto Condensed",Arial,sans-serif;font-weight:700;font-size:24px;color:var(--black);}
  .invest-title{left:227px;top:432px;}
  .chal-title{left:546px;top:432px;}
  .invest-table{left:223px;top:481px;width:311px;border-collapse:collapse;font-size:13.5px;}
  .invest-table td{padding:0 6px;height:24px;border-bottom:1px solid var(--white);}
  .invest-table td.amt{text-align:right;}
  .invest-table tr.gap td{border:none;height:28px;}
  .invest-table tr.sub td:first-child{border-bottom:none;}
  .challenges{left:546px;top:482px;width:350px;margin:0;padding:0;list-style:none;font-size:13.5px;line-height:16.3px;}
  .challenges li{position:relative;padding-left:17px;margin-bottom:16px;}
  .challenges li::before{content:"";position:absolute;left:0;top:6px;width:7px;height:7px;border-radius:50%;background:var(--black);}
  .map-panel{left:211px;top:806px;width:716px;height:394px;}
  .map-title{left:239px;top:836px;margin:0;font-family:"Roboto Condensed",Arial,sans-serif;font-weight:700;font-size:23px;color:var(--white);}
  .site-plan{left:246px;top:872px;width:520px;height:322px;background:linear-gradient(135deg,#9fd06a 0%,#c9c9c9 45%,#eeeeee 100%);border-radius:6px;}
  .foot-brand{left:30px;top:975px;width:170px;font-family:"Roboto",Arial,sans-serif;font-weight:400;color:var(--white);font-size:20px;line-height:23px;}
  .foot-address{left:30px;top:1096px;font-size:12px;line-height:15px;color:var(--white);}
</style>
</head>
<body>
<div class="page">
  <svg class="abs side-band" viewBox="0 0 204 1200" aria-hidden="true">
    <polygon points="0,40 46,80 46,0 204,0 204,1200 0,1200" fill="var(--blue)"/>
  </svg>

  <div class="abs brand-box"></div>
  <div class="abs brand-name">Pelvoran<br>Real Estate<br>Investments</div>

  <div class="abs header-band"></div>
  <h1 class="abs title">Morrowick Commons</h1>
  <p class="abs subtitle">Gilbert, Arizona</p>

  <svg class="abs corner" viewBox="0 0 210 165" aria-hidden="true">
    <polygon points="0,0 210,0 210,165" fill="var(--white)"/>
    <polygon points="12,0 210,0 210,150" fill="var(--gold)"/>
  </svg>
  <div class="abs profile-tag">Property<br>Profile</div>

  <div class="abs photo-frame"></div>
  <div class="abs photo before" role="img" aria-label="Photo of the shopping center before renovation"></div>
  <div class="abs photo after" role="img" aria-label="Rendering of the shopping center after renovation with new paint and signage"></div>

  <svg class="abs caption-band" viewBox="0 0 716 34" aria-hidden="true">
    <polygon points="0,0 716,0 716,34 38,34" fill="var(--black)"/>
  </svg>
  <div class="abs caption" style="left:407px">before</div>
  <div class="abs caption" style="left:843px">after</div>

  <div class="abs body-panel"></div>

  <h2 class="abs section-title invest-title">Investment</h2>
  <table class="abs invest-table">
    <tr><td>Purchase Price</td><td class="amt">$X,XXX,XXX</td></tr>
    <tr><td>Sponsor Acquisition Fee</td><td class="amt">$XX,XXX</td></tr>
    <tr><td>Painting and Landscape</td><td class="amt">$XXX,XXX</td></tr>
    <tr><td>TI/LC Reserve</td><td class="amt">$X,XXX,XXX</td></tr>
    <tr><td>Operating Expenses</td><td class="amt">$XXX,XXX</td></tr>
    <tr><td>Total Cash Investment</td><td class="amt"></td></tr>
    <tr class="gap"><td></td><td></td></tr>
    <tr><td>Investor / Sponsor Split</td><td class="amt">XX% / XX%</td></tr>
    <tr class="sub"><td>Structure</td><td class="amt">Cash Flow Pari Passu</td></tr>
    <tr class="sub"><td></td><td class="amt">Acquisition Fee</td></tr>
    <tr class="sub"><td></td><td class="amt">Management Fee</td></tr>
  </table>

  <h2 class="abs section-title chal-title">Challenges and Solutions</h2>
  <ul class="abs challenges">
    <li>Nationwide vacancy rate - Pelvoran did significant due diligence on the property before purchasing the asset, and determined that the location is an A/A-; Tenant improvement and leasing commissions were reserved in order to attract national and regional tenants</li>
    <li>Size of Anchor space - Pelvoran determined that a family-friendly entertainment venue would best serve the demographics in the area instead of another grocer; Pelvoran sought out an experienced operator in Tallow Cove, who has multiple locations in three states</li>
    <li>Curb Appeal - With vacancy and a stigma attached to the center, Pelvoran had to change the center’s appeal to the community. Pelvoran worked hand in hand with the Town of Gilbert and the Corvane Lakes community association to paint the center, upgrade landscaping and add new and larger monument signs</li>
  </ul>

  <svg class="abs map-panel" viewBox="0 0 716 394" aria-hidden="true">
    <polygon points="0,0 530,0 716,120 716,394 0,394" fill="var(--map-grey)"/>
  </svg>
  <h2 class="abs map-title">Morrowick Commons - 97% Occupancy</h2>
  <div class="abs site-plan" role="img" aria-label="Site plan of the center showing parking, pad buildings, the anchor tenant and surrounding roads"></div>

  <div class="abs foot-brand">Pelvoran<br>Real Estate<br>Investments</div>
  <div class="abs foot-address">2470 E Harlow Avenue Suite 12<br>Mesa, AZ 85200<br>(480) 555-0147</div>
</div>
</body>
</html>
```